Detail Shop Business card design

i need a business card design for my new detailing company called 'Brenner's Detail Shop'. i want an all black and white design . simple, direct and to the point. i want the designer to choose a fitting font to match the logothe front should have logo, address, phone and email and the back side should have a slogan and text indicating that we offer services on anything including cars, trucks, motorcycles and RVs. slogan will read "we take pride in your ride"
maybe also very small on the back side the IG icon with Brenners_Detail_Shop

phone 482.615.7734
address 7384 E Harlow Ave
Spokane WA 99342
email: BrennersDetail@quorvail.com

Target Market(s)

all ages , auto enthusiasts

Industry/Entity Type

Automotive

Contact Information for Business Card

the front should have logo, address, phone and email and the back side should have a slogan and text indicating that we offer services on anything including cars, trucks, motorcycles and RVs. slogan will read "we take pride in your ride"

phone 482.615.7734
address 7384 E Harlow Ave
Spokane WA 99342

Colors
000000
ffffff

Requirements
Must have
• bold font and very simple design with good spacing
Nice to have
• anything creative from the designer indicating we service any types of vehicles
Should not have
• any colors ,

```html
<!DOCTYPE html>
<html lang="en">
<head>
<meta charset="utf-8">
<title>Brenner's Detail Shop – Business Card</title>
<link rel="stylesheet" href="https://fonts.googleapis.com/css2?family=PT+Sans+Narrow:wght@400;700&display=swap">
<style>
  :root {
    --ink: #000000;
    --paper: #ffffff;
    --mid-grey: #9b9b9b;
    --soft-grey: #e9e9e9;
    --backdrop: #eef0ee;
  }
  html, body {
    margin: 0;
    padding: 0;
    width: 1200px;
    height: 1200px;
    overflow: hidden;
    background: var(--backdrop);
  }
  .canvas {
    position: relative;
    width: 1200px;
    height: 1200px;
  }
  .card {
    position: absolute;
    left: 211px;
    width: 779px;
    height: 444px;
    display: block;
  }
  .card--front { top: 140px; }
  .card--back { top: 645px; }
  .card text {
    font-family: "PT Sans Narrow", "Arial Narrow", sans-serif;
  }
  .brand-name { font-weight: 700; font-size: 46px; fill: var(--paper); letter-spacing: 0.5px; }
  .tagline { font-weight: 700; font-size: 25px; fill: var(--paper); letter-spacing: 1px; }
  .service { font-weight: 700; font-size: 30px; fill: var(--ink); }
  .mark-name { font-weight: 700; font-size: 21px; }
  .mark-name--light { fill: var(--paper); }
  .mark-name--dark { fill: var(--ink); }
  .contact { font-weight: 400; fill: var(--ink); }
  .contact--email { font-size: 22px; }
  .contact--phone { font-size: 27px; }
  .contact--address { font-size: 18px; }
  .contact--social { font-size: 23px; }
  .icon-fill { fill: var(--ink); }
  .icon-stroke { fill: none; stroke: var(--ink); stroke-width: 2.2; }
</style>
</head>
<body>
<main class="canvas">

  <!-- Front: name, slogan and services -->
  <svg class="card card--front" viewBox="0 0 779 444" xmlns="http://www.w3.org/2000/svg">
    <defs>
      <linearGradient id="servicesFade" x1="0" y1="0" x2="0" y2="1">
        <stop offset="0" stop-color="#ffffff"/>
        <stop offset="1" stop-color="#e6e6e6"/>
      </linearGradient>
    </defs>
    <rect class="card-base" width="779" height="444" fill="var(--paper)"/>
    <rect class="services-strip" x="0" y="340" width="779" height="104" fill="url(#servicesFade)"/>
    <rect class="grey-band" x="380" y="168" width="399" height="142" fill="var(--mid-grey)"/>
    <polygon class="black-band" points="0,138 461,138 645,340 0,340" fill="var(--ink)"/>

    <g class="brand-mark">
      <circle cx="38" cy="250" r="7" fill="var(--paper)"/>
      <text class="mark-name mark-name--light" x="52" y="245">BRENNER'S</text>
      <text class="mark-name mark-name--light" x="52" y="268">DETAIL SHOP</text>
    </g>

    <text class="brand-name" x="218" y="244">BRENNER'S DETAIL</text>
    <text class="tagline" x="206" y="286">WE TAKE PRIDE IN YOUR RIDE</text>

    <g class="services">
      <text class="service" x="92" y="420">» CARS</text>
      <text class="service" x="218" y="420">»TRUCKS</text>
      <text class="service" x="378" y="420">»MOTORCYCLES</text>
      <text class="service" x="620" y="420">»RVS</text>
    </g>
  </svg>

  <!-- Back: mark and contact details -->
  <svg class="card card--back" viewBox="0 0 779 444" xmlns="http://www.w3.org/2000/svg">
    <rect class="card-base" width="779" height="444" fill="var(--paper)"/>
    <polygon class="grey-top" points="0,0 779,0 779,72 470,72 545,126 0,126" fill="var(--mid-grey)"/>
    <polygon class="black-top" points="287,0 779,0 779,72 353,72" fill="var(--ink)"/>
    <rect class="mark-panel" x="0" y="126" width="395" height="166" fill="var(--paper)"/>
    <polygon class="grey-bottom" points="430,340 779,340 779,444 530,444" fill="var(--mid-grey)"/>
    <polygon class="black-bottom" points="0,292 370,292 530,444 0,444" fill="var(--ink)"/>

    <g class="brand-mark">
      <circle cx="132" cy="210" r="8" fill="var(--ink)"/>
      <text class="mark-name mark-name--dark" x="148" y="204">BRENNER'S</text>
      <text class="mark-name mark-name--dark" x="148" y="228">DETAIL SHOP</text>
    </g>

    <g class="contact-list">
      <g class="contact-row">
        <rect class="icon-fill" x="448" y="159" width="24" height="16"/>
        <polyline points="448,159 460,169 472,159" fill="none" stroke="var(--paper)" stroke-width="2"/>
        <text class="contact contact--email" x="495" y="175">BrennersDetail@quorvail.com</text>
      </g>
      <g class="contact-row">
        <path class="icon-fill" d="M453,206 l6,-3 l4,8 l-4,3 c2,5 5,8 9,10 l3,-4 l8,4 l-3,6 c-14,0 -24,-11 -23,-24 z"/>
        <text class="contact contact--phone" x="494" y="233">482.615.7734</text>
      </g>
      <g class="contact-row">
        <path class="icon-fill" d="M461,258 a9,9 0 0 1 9,9 c0,7 -9,17 -9,17 c0,0 -9,-10 -9,-17 a9,9 0 0 1 9,-9 z"/>
        <circle cx="461" cy="267" r="3.5" fill="var(--paper)"/>
        <text class="contact contact--address" x="491" y="283">7384 E Harlow Ave Spokane WA 99342</text>
      </g>
      <g class="contact-row">
        <rect class="icon-stroke" x="448" y="307" width="22" height="22"/>
        <text class="contact contact--social" x="490" y="325">Brenners_Detail_Shop</text>
      </g>
    </g>
  </svg>

</main>
</body>
</html>
```